Building Certification Company needs a professional letterhead and report template

We are a modern company within an ageing industry. Our industry is responsible for life safety aspects of the built environment, we ensure buildings are safe and fit for occupation.

We use letterhead and reports everyday, we need a smart and professional letterhead that reflects the serious nature of the work we do. We also require a report template of the same ilk.

Target Market(s)

Our target market will consist mainly of professional architects, developers and construction companies.

Requirements
Must have
• The letterhead must have:-
Our logo
Our company details, including address, website, email, phone

Address - Suite 208 / 43 Greyfern Avenue Tallowmere WR 9032

Website - www.harbourlinestructureaudits.com.au

Email - info@hlsa.com.au

Phone - 02 8364 5208

The report template must have:-
A title page, which is to incorporate our logo or an aspect of our logo, get creative people.

```html
<!DOCTYPE html>
<html lang="en">
<head>
<meta charset="utf-8">
<title>Harbourline Structure Audits – Stationery Set</title>
<link rel="stylesheet" href="https://fonts.googleapis.com/css2?family=Cinzel:wght@400;600&display=swap">
<style>
  :root{
    --bg:#e4e5e9;
    --paper:#ffffff;
    --brand:#2b38a3;
    --brand-deep:#1c2780;
    --brand-mid:#4753b9;
    --brand-pale:#aab0e2;
    --ink:#2a2a33;
    --shadow:0 6px 16px rgba(20,24,60,.18);
  }
  *{box-sizing:border-box;margin:0;padding:0}
  html,body{width:1200px;height:1000px;overflow:hidden;background:var(--bg);font-family:"Cinzel",serif}
  .canvas{position:relative;width:1200px;height:1000px}
  .sheet{position:absolute;background:var(--paper);box-shadow:var(--shadow);overflow:hidden}
  .sheet svg.bg{position:absolute;inset:0;width:100%;height:100%}

  .wordmark{position:absolute;font-family:"Cinzel",serif;font-weight:600;color:var(--brand);line-height:1.05;display:flex;align-items:center;gap:6px;white-space:nowrap}
  .wordmark .mark{width:12px;height:12px;background:currentColor;flex:none}
  .wordmark .name{display:flex;flex-direction:column;letter-spacing:.06em}
  .wordmark .name small{font-size:.62em;letter-spacing:.14em}
  .wordmark.on-dark{color:#fff}

  /* letterhead */
  .letterhead{left:330px;top:217px;width:400px;height:566px}
  .letterhead .wordmark.head{left:140px;top:44px;font-size:15px}
  .letter-body{position:absolute;left:112px;top:140px;width:262px;font-size:7.4px;line-height:1.45;color:var(--ink);text-transform:uppercase}
  .letter-body p{margin-bottom:8px}
  .letter-faint{position:absolute;left:150px;top:90px;width:230px;height:380px;opacity:.5}
  .letter-footer{position:absolute;right:18px;bottom:20px;font-size:5.6px;color:var(--brand);text-align:right;line-height:1.6;letter-spacing:.03em}
  .letterhead .wordmark.foot{left:20px;bottom:22px;font-size:7px;gap:4px}
  .letterhead .wordmark.foot .mark{width:9px;height:9px}

  /* report cover */
  .report{left:770px;top:217px;width:400px;height:566px}
  .report .wordmark.top{left:150px;top:70px;font-size:17px}
  .report .wordmark.bottom{left:170px;bottom:30px;font-size:12px}
  .report-art{position:absolute;left:150px;top:140px;width:230px;height:250px;opacity:.75}

  /* envelopes */
  .envelope{left:30px;width:280px;height:140px}
  .envelope.one{top:217px}
  .envelope.two{top:374px}
  .envelope .wordmark{left:14px;top:16px;font-size:9px}
  .envelope .return{position:absolute;left:32px;top:40px;font-size:4.2px;color:var(--brand);line-height:1.5;width:120px}
  .envelope .window{position:absolute;left:28px;top:72px;width:150px;height:40px;border-radius:6px;background:linear-gradient(#d9dadd,#eef0f2);border:1px solid #c4c6cc}

  /* business cards */
  .card{width:135px;height:78px}
  .card.front{background:var(--paper)}
  .card.back{background:var(--brand-mid)}
  .card.c1{left:30px;top:531px}
  .card.c2{left:175px;top:531px}
  .card.c3{left:30px;top:623px}
  .card.c4{left:175px;top:623px}
  .card.front .wordmark{left:50%;top:50%;transform:translate(-50%,-50%);font-size:11px}
  .card.back .wordmark{left:10px;top:8px;font-size:6.5px}
  .card-art{position:absolute;left:28px;top:22px;width:96px;height:50px;opacity:.8}
</style>
</head>
<body>
<main class="canvas">

  <section class="sheet letterhead" aria-label="Letterhead">
    <svg class="bg" viewBox="0 0 400 566" preserveAspectRatio="none" aria-hidden="true">
      <defs>
        <linearGradient id="lh-blue" x1="0" y1="0" x2="1" y2="1">
          <stop offset="0" stop-color="#3340ad"/><stop offset="1" stop-color="#4652bb"/>
        </linearGradient>
      </defs>
      <rect width="400" height="566" fill="url(#lh-blue)"/>
      <ellipse cx="350" cy="250" rx="330" ry="400" fill="#fff"/>
    </svg>
    <div class="letter-faint" role="img" aria-label="Faint brand stripe decoration" style="background:linear-gradient(160deg,rgba(43,56,163,.05),rgba(43,56,163,.12))"></div>
    <div class="wordmark head"><span class="mark"></span><span class="name">HARBOURLINE<small>Structure Audits</small></span></div>
    <div class="letter-body">
      <p>Letterhead Design</p>
      <p>Task Outline</p>
      <p>Create a Letterhead Design</p>
      <p>Task Description<br>We are a modern company within an ageing industry. Our industry is responsible for life safety aspects of the built environment, we ensure buildings are safe and fit for occupation.</p>
      <p>We use letterhead and reports everyday, we need a smart and professional letterhead that reflects the serious nature of the work we do. We also require a report template of the same ilk.</p>
      <p>Deadline<br>Tuesday, December 10, 2013</p>
      <p>Target Market(s)<br>Our target market will consist mainly of professional architects, developers and construction companies.</p>
      <p>Look and Feel<br>Each slider illustrates characteristics of the customer's brand and the style your design should communicate.</p>
    </div>
    <div class="letter-footer">Suite 208 / 43 Greyfern Avenue Tallowmere WR 9032 &nbsp;|&nbsp; 02 8364 5208<br>info@hlsa.com.au &nbsp;|&nbsp; www.harbourlinestructureaudits.com.au</div>
    <div class="wordmark on-dark foot"><span class="mark"></span><span class="name">HARBOURLINE<small>Structure Audits</small></span></div>
  </section>

  <section class="sheet report" aria-label="Report title page">
    <svg class="bg" viewBox="0 0 400 566" preserveAspectRatio="none" aria-hidden="true">
      <defs>
        <radialGradient id="rp-blue" cx=".6" cy=".35" r=".7">
          <stop offset="0" stop-color="#3a47b3"/><stop offset="1" stop-color="#1c2780"/>
        </radialGradient>
      </defs>
      <rect width="400" height="566" fill="#fff"/>
      <circle cx="440" cy="190" r="320" fill="url(#rp-blue)"/>
    </svg>
    <div class="report-art" role="img" aria-label="Large brand stripe decoration" style="background:linear-gradient(150deg,rgba(170,176,226,.35),rgba(170,176,226,.6))"></div>
    <div class="wordmark on-dark top"><span class="name">HARBOURLINE<small>Structure Audits</small></span></div>
    <div class="wordmark bottom"><span class="mark"></span><span class="name">HARBOURLINE<small>Structure Audits</small></span></div>
  </section>

  <section class="sheet envelope one" aria-label="Envelope">
    <svg class="bg" viewBox="0 0 280 140" preserveAspectRatio="none" aria-hidden="true">
      <path d="M170 0 H280 V140 H258 C258 70 225 22 170 0 Z" fill="var(--brand)"/>
      <path d="M200 0 H280 V120 C270 60 245 20 200 0 Z" fill="#fff"/>
      <rect x="236" y="8" width="8" height="132" fill="var(--brand-mid)"/>
    </svg>
    <div class="wordmark"><span class="mark"></span><span class="name">HARBOURLINE<small>Structure Audits</small></span></div>
    <div class="return">Suite 208 / 43 Greyfern Avenue<br>Tallowmere WR 9032</div>
    <div class="window"></div>
  </section>

  <section class="sheet envelope two" aria-label="Envelope">
    <svg class="bg" viewBox="0 0 280 140" preserveAspectRatio="none" aria-hidden="true">
      <path d="M170 0 H280 V140 H258 C258 70 225 22 170 0 Z" fill="var(--brand)"/>
      <path d="M200 0 H280 V120 C270 60 245 20 200 0 Z" fill="#fff"/>
      <rect x="236" y="8" width="8" height="132" fill="var(--brand-mid)"/>
    </svg>
    <div class="wordmark"><span class="mark"></span><span class="name">HARBOURLINE<small>Structure Audits</small></span></div>
    <div class="return">Suite 208 / 43 Greyfern Avenue<br>Tallowmere WR 9032</div>
    <div class="window"></div>
  </section>

  <section class="sheet card front c1" aria-label="Business card front">
    <div class="wordmark"><span class="mark"></span><span class="name">HARBOURLINE<small>Structure Audits</small></span></div>
  </section>
  <section class="sheet card back c2" aria-label="Business card back">
    <div class="wordmark on-dark"><span class="name">HARBOURLINE<small>Structure Audits</small></span></div>
    <div class="card-art" role="img" aria-label="Brand stripe decoration" style="background:linear-gradient(150deg,rgba(255,255,255,.25),rgba(255,255,255,.55))"></div>
  </section>
  <section class="sheet card back c3" aria-label="Business card back">
    <div class="wordmark on-dark"><span class="name">HARBOURLINE<small>Structure Audits</small></span></div>
    <div class="card-art" role="img" aria-label="Brand stripe decoration" style="background:linear-gradient(150deg,rgba(255,255,255,.25),rgba(255,255,255,.55))"></div>
  </section>
  <section class="sheet card front c4" aria-label="Business card front">
    <div class="wordmark"><span class="mark"></span><span class="name">HARBOURLINE<small>Structure Audits</small></span></div>
  </section>

</main>
</body>
</html>
```